Help Meadowlane Ledger create a brochure with great copy!

I would like a double sided 11"x17" brochure designed. It will be fold in half to form a book (like this: http://www.quickfolioprints.example/summer/cart1/images/uploads/11x17bro.jpg)

It will have 4 sides, front/back and inside left/inside right.

We are building intuitive software to help farmers make better farm finance decisions. It's important to note that every farm is unique and our team of advisors will be standing by to help users with the software and to help them with specific decisions for their operation.

Our software will have the following features which I want to be highlighted in the brochure.

1 - Field-by-Field Budget Tracker (Here you'll show the Inputs screen and the Applications screen). The Inputs section is where users will track their yearly input variable and overhead expenses (seed, fertilizer, chemical, crop insurance, repairs, fuel, drying, crop insurance, debt payments, and misc. expenses). The Applications section is where users will easily assign these expenses to each field they farm.

They will build their budget before the growing season and adjust that budget to actual during the growing season.

2 - Field-by-Field Profit and Loss Tracking (where you'll show the field-by-field P&L screenshot). Users will be able to track their budgets on a field-by-field basis both yearly and cumulatively. This will give them better insight into which fields are the most profitable for their farm or which are costing them money. If fields are costing them money over the long-term, they can either choose to improve the fields or drop them.

3 - Grain Marketing Plan Builder (include the Marketing Plan Screenshot). This is where users can build a time and profit-based grain marketing plan. Most users make grain marketing (when, where, and at what price to sell) based on gut feel and emotion. Our grain marketing plan builder allows farmers to build a structured grain marketing plan.

4 - Grain Contract Tracking (include Grain Contract tracking screenshot). This is where users can track their current grain sales and contracts. Contract types include cash sales, forward contracts, basis contracts, hedge-to-arrive contracts, futures hedges, and option strategies. Throughout the growing season, users will be able to quickly analyze how much grain they have contracted and how much they have available to market.

Other features include futures markets, cash markets, market news and commentary, what/if analysis tools, educational materials, and personalized recommendations.
__________________________

Today's farmer wears many hats. They are typically the CEO, the Director of HR, the CFO, the Agronomist and the Mechanic. Farm risk management and finance often get overlooked when they are a huge driver of farm profits and losses. Our software combined with our staff of advisors will become a partner in their farming operation ensuring that they can survive and thrive during today's tough farm economy.

Rather than making decisions guided by gut feel and emotion, our software allows farmers to professionalize their farm finance and risk management.

Being a great farm finance manager is no longer a trait of the most successful farms, its necessity of all farms.

Please include farm focused-pictures from Pixorama. Pictures of wheat or corn fields.

I would like you to add additional sales-focused copy.

Meadowlane Ledger's address is 2817 Belwyn Pkwy S, Fargo, ND 58102. Contact is Tom Walsey (tomw@cropledgerservices.example) and 701-555-0148.

Target Market(s)

Agriculture, Farmers

Font styles to use
Sans Serif

Colors
acd036
9bcb3b

Requirements
Must have
• Good copy. Highlight software features and personalize service from advisors

```html
<!DOCTYPE html>
<html lang="en">
<head>
<meta charset="utf-8">
<title>Meadowlane Ledger – Back Cover</title>
<link href="https://fonts.googleapis.com/css2?family=Rajdhani:wght@500&family=Open+Sans:wght@400&display=swap" rel="stylesheet">
<style>
  :root {
    --backdrop: #9d9d9f;
    --sky-top: #8fa7a0;
    --sky-mid: #d9d6c8;
    --wheat-light: #d8bf8e;
    --wheat-deep: #a9823f;
    --band: rgba(238, 230, 214, 0.72);
    --strip: #b58a3c;
    --ink: #4a4540;
    --ink-soft: #6a625a;
  }
  * { margin: 0; padding: 0; box-sizing: border-box; }
  html, body {
    width: 1200px; height: 803px; overflow: hidden;
    background: var(--backdrop);
  }
  .stage {
    width: 1200px; height: 803px;
    display: flex; align-items: center; justify-content: center;
  }
  .back-cover {
    position: relative;
    width: 572px; height: 740px;
    overflow: hidden;
    box-shadow: 0 6px 18px rgba(0,0,0,0.25);
  }
  .cover-photo {
    position: absolute; inset: 0;
    background:
      radial-gradient(ellipse at 45% 25%, rgba(245,242,232,0.85), transparent 55%),
      linear-gradient(180deg, var(--sky-top) 0%, var(--sky-mid) 30%, var(--wheat-light) 55%, var(--wheat-deep) 100%);
  }
  .contact-band {
    position: absolute; left: 0; right: 0;
    top: 474px; height: 150px;
    background: var(--band);
    display: flex; align-items: center;
    padding: 0 34px 0 40px;
    gap: 40px;
  }
  .brand { display: flex; flex-direction: column; gap: 4px; width: 230px; }
  .brand-name {
    display: flex; align-items: center; gap: 8px;
    font-family: "Rajdhani", sans-serif; font-weight: 500;
    font-size: 24px; letter-spacing: 0.5px; color: var(--ink);
    text-transform: uppercase; line-height: 1;
  }
  .brand-mark {
    width: 20px; height: 20px; border-radius: 50%;
    background: var(--ink); flex: none;
  }
  .brand-tagline {
    font-family: "Open Sans", sans-serif; font-size: 11.5px;
    color: var(--ink-soft); letter-spacing: 0.4px; padding-left: 28px;
  }
  .contact-list { list-style: none; display: flex; flex-direction: column; gap: 10px; }
  .contact-item {
    display: flex; align-items: center; gap: 12px;
    font-family: "Open Sans", sans-serif; font-size: 9.5px;
    color: var(--ink-soft); letter-spacing: 0.2px;
  }
  .contact-item svg { width: 16px; height: 14px; flex: none; fill: var(--ink); }
  .gold-strip {
    position: absolute; left: 0; right: 0;
    top: 624px; height: 22px;
    background: var(--strip); opacity: 0.85;
  }
</style>
</head>
<body>
<main class="stage">
  <section class="back-cover">
    <div class="cover-photo" role="img" aria-label="Close-up photograph of golden wheat ears swaying against a cloudy sky"></div>

    <div class="contact-band">
      <div class="brand">
        <div class="brand-name"><span class="brand-mark"></span>Meadowlane Ledger</div>
        <div class="brand-tagline">Farm Risk Management Software</div>
      </div>

      <ul class="contact-list">
        <li class="contact-item">
          <svg viewBox="0 0 16 12" aria-hidden="true"><path d="M0 0h16v12H0z M1.5 1.5 8 6.5l6.5-5V10.5h-13z" fill-rule="evenodd"/></svg>
          <span>MEADOWLANE LEDGER, 2817 BELWYN PARKWAY S</span>
        </li>
        <li class="contact-item">
          <svg viewBox="0 0 16 14" aria-hidden="true"><path d="M1 4c3-3 11-3 14 0l-1 2-3-1V3.5C9.5 3 6.5 3 5 3.5V5L2 6z M4 7h8l2 6H2z"/></svg>
          <span>FARGO, ND 58102 (701)-555-0148</span>
        </li>
        <li class="contact-item">
          <svg viewBox="0 0 16 14" aria-hidden="true"><path d="M4 0h8v4H4z M1 5h14v9H1z M4 8h8v1H4z M4 10.5h8v1H4z" fill-rule="evenodd"/></svg>
          <span>(701)-555-0148</span>
        </li>
        <li class="contact-item">
          <svg viewBox="0 0 16 12" aria-hidden="true"><path d="M0 0h16v12H0z M1.5 1.5 8 6.5l6.5-5V10.5h-13z" fill-rule="evenodd"/></svg>
          <span>tomw@cropledgerservices.example</span>
        </li>
        <li class="contact-item">
          <svg viewBox="0 0 16 16" aria-hidden="true"><path d="M8 0a8 8 0 1 0 0 16A8 8 0 0 0 8 0zm0 1.5a6.5 6.5 0 0 1 0 13 6.5 6.5 0 0 1 0-13zM2 7.3h12v1.4H2zM7.3 2h1.4v12H7.3z"/></svg>
          <span>www.meadowlaneledger.example</span>
        </li>
      </ul>
    </div>

    <div class="gold-strip"></div>
  </section>
</main>
</body>
</html>
```